Swimming Pool Supply Company Business Cards

We need business cards designed for company. These need to be easy to edit so that we can fill in names, titles, and contact info for each person who works here.

Dalton R. Pembry
Manager of Legal & Finance
J.L. Pembry, Incorporated

4837 Grelwood Avenue
Marlow Crossing, PA 19054

E. dalton@jlpembry.com
M. (215) 555-7193
O. (215) 555-4620

Contact Information for Business Card

Looking to upgrade current business cards with graphic that can be edited. Looking for fresh ideas for an age old industry.

Font styles to use
Serif
Sans Serif

Colors

Designer to choose colors to be used in the design.

Requirements
Must have
• Professional, fresh, unique but professional

```html
<!DOCTYPE html>
<html lang="en">
<head>
<meta charset="utf-8">
<title>Pembry Business Card</title>
<link href="https://fonts.googleapis.com/css2?family=Roboto+Condensed:wght@700&family=Roboto:wght@300;400&display=swap" rel="stylesheet">
<style>
  :root {
    --page-bg: #e9e6e2;
    --card-top: #34383b;
    --card-bottom: #222527;
    --brand-blue: #1c8fd3;
    --brand-blue-light: #35a7e6;
    --band-blue-dark: #0f5f8f;
    --text-light: #d9dcde;
    --text-muted: #b9b3b3;
    --icon-blue: #1f86c4;
  }
  html, body {
    margin: 0;
    padding: 0;
    width: 1200px;
    height: 1054px;
    overflow: hidden;
    background: var(--page-bg);
  }
  .business-card {
    position: absolute;
    left: 80px;
    top: 213px;
    width: 1040px;
    height: 628px;
    background: linear-gradient(160deg, var(--card-top), var(--card-bottom));
    box-shadow: 0 14px 40px rgba(0,0,0,0.25);
    overflow: hidden;
    font-family: "Roboto", Arial, sans-serif;
  }
  .brand-name {
    position: absolute;
    left: 49px;
    top: 70px;
    margin: 0;
    font-family: "Roboto Condensed", "Arial Narrow", sans-serif;
    font-weight: 700;
    font-size: 150px;
    line-height: 1;
    letter-spacing: 4px;
    color: var(--brand-blue);
  }
  .brand-tagline {
    position: absolute;
    left: 99px;
    top: 220px;
    margin: 0;
    font-size: 22px;
    font-weight: 400;
    letter-spacing: 0.3px;
    color: var(--brand-blue);
  }
  .person-name {
    position: absolute;
    left: 49px;
    top: 355px;
    margin: 0;
    font-family: "Roboto Condensed", "Arial Narrow", sans-serif;
    font-weight: 700;
    font-size: 41px;
    color: var(--brand-blue);
  }
  .person-title {
    position: absolute;
    left: 49px;
    top: 403px;
    margin: 0;
    font-size: 25px;
    font-weight: 400;
    color: var(--text-light);
  }
  .office-address {
    position: absolute;
    left: 49px;
    top: 478px;
    margin: 0;
    font-style: normal;
    font-size: 25px;
    line-height: 37px;
    color: var(--text-muted);
  }
  .contact-list {
    position: absolute;
    left: 628px;
    top: 351px;
    margin: 0;
    padding: 0;
    list-style: none;
  }
  .contact-item {
    display: flex;
    align-items: center;
    height: 37px;
    font-size: 25px;
    font-weight: 400;
    color: var(--text-light);
  }
  .contact-icon {
    width: 22px;
    height: 22px;
    margin-right: 28px;
    fill: var(--icon-blue);
  }
  .company-band {
    position: absolute;
    right: 0;
    bottom: 0;
    width: 540px;
    height: 78px;
  }
  .company-band svg {
    position: absolute;
    inset: 0;
  }
  .company-name {
    position: absolute;
    left: 113px;
    top: 22px;
    margin: 0;
    font-size: 25px;
    font-weight: 400;
    color: #c9d3d9;
  }
  .card-foot {
    position: absolute;
    left: 0;
    bottom: 0;
    width: 100%;
    height: 24px;
    background: rgba(255,255,255,0.08);
  }
</style>
</head>
<body>
  <div class="business-card">
    <h1 class="brand-name">PEMBRY</h1>
    <p class="brand-tagline">SWIMMING POOLS, SUPPLIES &amp; ACCESSORIES</p>

    <h2 class="person-name">Dalton R. Pembry</h2>
    <p class="person-title">Manager of Legal &amp; Finance</p>
    <address class="office-address">4837 Grelwood Avenue<br>Marlow Crossing, PA 19054</address>

    <ul class="contact-list">
      <li class="contact-item">
        <svg class="contact-icon" viewBox="0 0 24 24" aria-hidden="true"><path d="M7 1h10a2 2 0 0 1 2 2v18a2 2 0 0 1-2 2H7a2 2 0 0 1-2-2V3a2 2 0 0 1 2-2zm0 3v14h10V4zm5 15.5a1.2 1.2 0 1 0 0 2.4 1.2 1.2 0 0 0 0-2.4z"/></svg>
        (215) 555-7193
      </li>
      <li class="contact-item">
        <svg class="contact-icon" viewBox="0 0 24 24" aria-hidden="true"><path d="M2 8c0-3 4-5 10-5s10 2 10 5v2h-5V8c-1-1-3-1.5-5-1.5S8 7 7 8v2H2zm4 4h12l3 9H3zm6 2a2.5 2.5 0 1 0 0 5 2.5 2.5 0 0 0 0-5z"/></svg>
        (215) 555-4620
      </li>
      <li class="contact-item">
        <svg class="contact-icon" viewBox="0 0 24 24" aria-hidden="true"><path d="M2 5h20v14H2zm2 2v.5l8 5.5 8-5.5V7zm0 3v7h16v-7l-8 5.5z"/></svg>
        dalton@jlpembry.com
      </li>
      <li class="contact-item">
        <svg class="contact-icon" viewBox="0 0 24 24" aria-hidden="true"><path d="M12 2a10 10 0 1 0 0 20 10 10 0 0 0 0-20zm0 2c1.2 1.3 2.1 3.3 2.4 7H9.6c.3-3.7 1.2-5.7 2.4-7zM7.6 11H4.1a8 8 0 0 1 5-6.4C8.2 6.2 7.7 8.4 7.6 11zm8.8 0c-.1-2.6-.6-4.8-1.5-6.4a8 8 0 0 1 5 6.4zM4.1 13h3.5c.1 2.6.6 4.8 1.5 6.4a8 8 0 0 1-5-6.4zm5.5 0h4.8c-.3 3.7-1.2 5.7-2.4 7-1.2-1.3-2.1-3.3-2.4-7zm6.8 0h3.5a8 8 0 0 1-5 6.4c.9-1.6 1.4-3.8 1.5-6.4z"/></svg>
        www.jlpembry.com
      </li>
    </ul>

    <div class="card-foot"></div>

    <div class="company-band">
      <svg width="540" height="78" viewBox="0 0 540 78" aria-hidden="true">
        <defs>
          <linearGradient id="bandGradient" x1="0" y1="0" x2="1" y2="1">
            <stop offset="0" stop-color="#1a7fb8"/>
            <stop offset="0.5" stop-color="#2ea3e0"/>
            <stop offset="1" stop-color="#0f5f8f"/>
          </linearGradient>
        </defs>
        <path d="M40 0 H540 V78 H0 Q20 8 40 0 Z" fill="url(#bandGradient)"/>
      </svg>
      <p class="company-name">J.L. Pembry, Incorporated</p>
    </div>
  </div>
</body>
</html>
```